Brochure for social media influencers for our beauty clinic

We need a 10 page brochure for our beauty clinic.<br/>FRONT PAGE<br/>ABOUT US (double spread - detailing what we do at our clinic and the services we offer - also what services are complimentary for influencers)<br/>TRAVEL (double spread - detailing travel options and the purchasing of train tickets)<br/><br/>ACCOMADATION (double spread - we are in partnership with the marlow lodge and spa so we detail the room spec and what services and amenities are on-site etc)<br/>WHAT WE NEED FROM YOU (double spread - what the influencer needs to do for us to help promote our business etc)<br/>BACK PAGE

Target Market(s)

Social media influencers - 18-40 years old.

Industry/Entity Type

Beauty

Font styles to use
Sans Serif

Requirements
Must have
• Minimalism, greys, anthracites, modern look.
Should not have
• No tackiness. Needs to be clean and modern

```html
<!DOCTYPE html>
<html lang="en">
<head>
<meta charset="UTF-8">
<title>Beauty Clinic Influencer Brochure</title>
<link href="https://fonts.googleapis.com/css2?family=Montserrat:wght@500;600;700&family=Questrial&display=swap" rel="stylesheet">
<style>
  :root {
    --canvas: #e4e4e4;
    --panel: #000000;
    --ink: #ffffff;
    --ink-soft: #d9d9d9;
    --blush: #f2a7b4;
    --blush-deep: #e88e9f;
  }
  * { box-sizing: border-box; margin: 0; padding: 0; }
  html, body { width: 1200px; height: 1200px; overflow: hidden; }
  body {
    background: radial-gradient(circle at 50% 40%, #f0f0f0, var(--canvas));
    font-family: "Questrial", sans-serif;
    color: var(--ink);
    position: relative;
  }
  .spread {
    position: absolute;
    display: flex;
    box-shadow: 0 18px 30px rgba(0,0,0,0.18);
  }
  .spread--cover { left: 337px; top: 59px; width: 526px; height: 281px; }
  .spread--about { left: 37px; top: 440px; width: 541px; height: 279px; }
  .spread--travel { left: 624px; top: 440px; width: 541px; height: 279px; }
  .spread--stay { left: 37px; top: 807px; width: 541px; height: 279px; }
  .spread--need { left: 624px; top: 807px; width: 541px; height: 279px; }
  .page { flex: 0 0 50%; width: 50%; min-width: 0; position: relative; overflow: hidden; }
  .page--dark { background: var(--panel); padding: 48px 18px 0 18px; }
  .photo {
    position: absolute; inset: 0;
    display: flex; align-items: center; justify-content: center;
  }
  .photo--portrait { background: linear-gradient(160deg, var(--blush), var(--blush-deep)); }
  .photo--doctor { background: linear-gradient(150deg, #c9ced3, #8e9499 70%, #b8b2aa); }
  .photo--travel { background: linear-gradient(160deg, #4a4442, #2a2625 70%, #1e1b1a); }
  .photo--hotel { background: linear-gradient(180deg, #5577b0 0%, #5b4a44 45%, #2e2722 100%); }
  .photo--desk { background: linear-gradient(150deg, #e8e4e1, #b9aea7 60%, #d6d3d2); }
  .feature-title {
    font-family: "Montserrat", sans-serif;
    font-weight: 600;
    color: var(--ink);
    text-align: center;
    line-height: 1.1;
    letter-spacing: -0.5px;
    text-shadow: 0 1px 6px rgba(0,0,0,0.25);
  }
  .feature-title--about { font-size: 32px; }
  .feature-title--travel { font-size: 46px; font-weight: 700; }
  .feature-title--stay { font-size: 24px; }
  .feature-title--need { font-size: 25px; }
  .brand-name {
    position: absolute; left: 0; right: 0; bottom: 22px;
    text-align: center;
    font-family: "Montserrat", sans-serif;
    font-weight: 600; font-size: 28px; color: var(--ink);
  }
  .section-heading {
    font-family: "Montserrat", sans-serif;
    font-weight: 600;
    font-size: 11px;
    text-transform: uppercase;
    margin-bottom: 6px;
    white-space: nowrap;
  }
  .body-copy {
    font-size: 5.8px; line-height: 1.42; color: var(--ink-soft);
    padding-left: 11px; max-width: 230px;
  }
  .list { list-style: none; font-size: 5.6px; line-height: 1.45; color: var(--ink-soft); padding-left: 11px; }
  .list li span { display: block; padding-left: 9px; }
  .section + .section { margin-top: 36px; }
  .contact-heading {
    position: absolute; left: 19px; top: 42px;
    font-family: "Montserrat", sans-serif; font-weight: 600; font-size: 11px;
  }
  .contact-list {
    position: absolute; left: 177px; top: 186px;
    border-left: 1px solid var(--ink);
    padding: 2px 0 2px 6px;
    list-style: none;
  }
  .contact-list li {
    display: flex; align-items: center; gap: 7px;
    font-size: 4.6px; height: 11.5px; white-space: nowrap;
  }
  .contact-list svg { width: 7px; height: 7px; fill: var(--ink); flex: none; }
</style>
</head>
<body>

<section class="spread spread--cover">
  <div class="page">
    <div class="photo photo--portrait" role="img" aria-label="Portrait of a woman with clear skin, hands framing her face, on a pink backdrop"></div>
    <div class="brand-name">Orlenne Clinic</div>
  </div>
  <div class="page page--dark">
    <h2 class="contact-heading">CONTACT US</h2>
    <ul class="contact-list">
      <li><svg viewBox="0 0 10 10"><path d="M5 0a3.5 3.5 0 0 0-3.5 3.5C1.5 6 5 10 5 10s3.5-4 3.5-6.5A3.5 3.5 0 0 0 5 0zm0 5a1.4 1.4 0 1 1 0-2.8A1.4 1.4 0 0 1 5 5z"/></svg>Street address, City</li>
      <li><svg viewBox="0 0 10 10"><path d="M2 0l2 2.5-1 1.2a6 6 0 0 0 3.3 3.3l1.2-1L10 8l-1.5 2C4 10 0 6 0 1.5z"/></svg>(123) 456-7890</li>
      <li><svg viewBox="0 0 10 10"><path d="M2.5 0h5v10h-5zM3.3 1v7h3.4V1z"/></svg>(123) 456-7890</li>
      <li><svg viewBox="0 0 10 10"><path d="M0 3h2v7H0zM3 0h4v3h3v7H3zm1 4h1v1H4zm2 0h1v1H6zm2 0h1v1H8zM4 6h1v1H4zm2 0h1v1H6zm2 0h1v1H8z"/></svg>(123) 456-7890</li>
      <li><svg viewBox="0 0 10 10"><path d="M0 1.5h10v7H0zm.8.8L5 5.5l4.2-3.2z"/></svg>info@yourwebsite.com</li>
      <li><svg viewBox="0 0 10 10"><path d="M2 0l6.5 6.2-3 .2 1.8 3.3-1.2.6-1.8-3.3L2 9z"/></svg>www.yourwebsite.com</li>
    </ul>
  </div>
</section>

<section class="spread spread--about">
  <div class="page">
    <div class="photo photo--doctor" role="img" aria-label="Smiling clinician in a white coat at a desk with a laptop">
      <h1 class="feature-title feature-title--about">ABOUT US</h1>
    </div>
  </div>
  <div class="page page--dark">
    <div class="section">
      <h2 class="section-heading">About Us</h2>
      <p class="body-copy">We need a 10 page brochure for our beauty clinic. FRONT PAGE. ABOUT US (double spread - detailing what we do at our clinic and the services we offer - also what services are complimentary for influencers). TRAVEL (double spread - detailing travel options and the purchasing of train tickets). ACCOMADATION (double spread - we are in partnership with the marlow lodge and spa so we detail the room spec and what services and amenities are on-site etc). WHAT WE NEED FROM YOU (double spread - what the influencer needs to do for us to help promote our business etc). BACK PAGE</p>
    </div>
    <div class="section">
      <h2 class="section-heading">Our Services</h2>
      <ul class="list">
        <li>- Service one.<span>what we do at our clinic and the services we offer.</span></li>
        <li>- Service two.<span>what we do at our clinic and the services we offer.</span></li>
        <li>- Service three.<span>what we do at our clinic and the services we offer.</span></li>
        <li>- Service four.<span>what we do at our clinic and the services we offer.</span></li>
        <li>- Service five.<span>what we do at our clinic and the services we offer.</span></li>
      </ul>
    </div>
  </div>
</section>

<section class="spread spread--travel">
  <div class="page">
    <div class="photo photo--travel" role="img" aria-label="Travel flat lay with straw hat, toy plane, map, sunglasses and camera on dark wood">
      <h1 class="feature-title feature-title--travel">TRAVEL</h1>
    </div>
  </div>
  <div class="page page--dark">
    <div class="section">
      <h2 class="section-heading">Travel Options</h2>
      <ul class="list">
        <li>- Option one.<span>Detailing travel options and the purchasing of train tickets.</span></li>
        <li>- Option two.<span>Detailing travel options and the purchasing of train tickets.</span></li>
        <li>- Option three.<span>Detailing travel options and the purchasing of train tickets.</span></li>
        <li>- Option four.<span>Detailing travel options and the purchasing of train tickets.</span></li>
        <li>- Option five.<span>Detailing travel options and the purchasing of train tickets.</span></li>
        <li>- Option six.<span>Detailing travel options and the purchasing of train tickets.</span></li>
      </ul>
    </div>
  </div>
</section>

<section class="spread spread--stay">
  <div class="page">
    <div class="photo photo--hotel" role="img" aria-label="Brick lodge entrance at dusk with lit Christmas trees either side">
      <h1 class="feature-title feature-title--stay">ACCOMADATION</h1>
    </div>
  </div>
  <div class="page page--dark">
    <div class="section">
      <h2 class="section-heading">Accomadation</h2>
      <p class="body-copy">We need a 10 page brochure for our beauty clinic. FRONT PAGE. ABOUT US (double spread - detailing what we do at our clinic and the services we offer - also what services are complimentary for influencers). TRAVEL (double spread - detailing travel options and the purchasing of train tickets). ACCOMADATION (double spread - we are in partnership with the marlow lodge and spa so we detail the room spec and what services and amenities are on-site etc). WHAT WE NEED FROM YOU (double spread - what the influencer needs to do for us to help promote our business etc). BACK PAGE</p>
    </div>
    <div class="section">
      <h2 class="section-heading">Room Spec - Services - Amenities</h2>
      <p class="body-copy">We need a 10 page brochure for our beauty clinic. FRONT PAGE. ABOUT US (double spread - detailing what we do at our clinic and the services we offer - also what services are complimentary for influencers). TRAVEL (double spread - detailing travel options and the purchasing of train tickets). ACCOMADATION (double spread - we are in partnership with the marlow lodge and spa so we detail the room spec and what services and amenities are on-site etc). WHAT WE NEED FROM YOU (double spread - what the influencer needs to do for us to help promote our business etc). BACK PAGE</p>
    </div>
  </div>
</section>

<section class="spread spread--need">
  <div class="page">
    <div class="photo photo--desk" role="img" aria-label="Young woman working thoughtfully at a laptop in a bright room">
      <h1 class="feature-title feature-title--need">WHAT WE NEED<br>FROM YOU</h1>
    </div>
  </div>
  <div class="page page--dark">
    <div class="section">
      <h2 class="section-heading">What We Need From You</h2>
      <p class="body-copy">We need a 10 page brochure for our beauty clinic. FRONT PAGE. ABOUT US (double spread - detailing what we do at our clinic and the services we offer - also what services are complimentary for influencers). TRAVEL (double spread - detailing travel options and the purchasing of train tickets). ACCOMADATION (double spread - we are in partnership with the marlow lodge and spa so we detail the room spec and what services and amenities are on-site etc). WHAT WE NEED FROM YOU (double spread - what the influencer needs to do for us to help promote our business etc). BACK PAGE</p>
    </div>
  </div>
</section>

</body>
</html>
```